Business Card Design Project - KLB

I am looking for a more sophisticated card design for my company,
"The Kestrel Bureau"

We are a consultancy focused on strategy and change in Associations and professional organisations.

I am a lawyer and psychologist with a PhD and so am looking for something that communicates seriousness and credibility but also quirky creative solutions for strategic problems, which is my field of speciality.

I am looking for something that is quietly spoken, rather than loud colours ('credible' and 'creative' are the two adjectives that I think of as competing here).

I particularly like an embossed card style - heavy white card with plain white or white and black or white and grey text.

The key logo image for the company is a question mark and I am open to suggestions and ideas on design.

I have attached a file that includes a couple of styles that have caught my eye and my thoughts on them. Hopefully they communicate what I'm looking for.
Updates

Thank you for all the great suggestions and designs.

I really appreciated the effort and creative energy you put into your designs. I have now closed the project after selecting a design and advising the successful designer of the card that I am happy with.

Regards

Target Market(s)

Organisations (CEO's and Boards), Governments, Legal professionals, Membership Associations and aspiring professionals.

Industry/Entity Type

Lawyer

Requirements
Must have
• The key logo element is a question mark (?) and this needs to be incorporated.

Embossed style - cut outs or other design ideas interest me too.

The attached file has a number of sample ideas and comments on each one that I like.
Should not have
• I like crisp, modern fonts (Myriads etc...) and do not like embellished fonts or Times etc...

```html
<!DOCTYPE html>
<html lang="en">
<head>
<meta charset="utf-8">
<title>The Kestrel Bureau – Business Card</title>
<link href="https://fonts.googleapis.com/css2?family=Jost:wght@300;400&display=swap" rel="stylesheet">
<style>
  :root {
    --page: #ffffff;
    --band-light: #7b7b7b;
    --panel: #5b5b5b;
    --edge: #777777;
    --back: #5d5d5d;
    --stripe: #4c4c4c;
    --ink-light: #d4d4d4;
    --ink-soft: #b8b8b8;
    --ink-muted: #9a9a9a;
    --mark: #7c7c7c;
  }
  * { margin: 0; padding: 0; box-sizing: border-box; }
  html, body { width: 1200px; height: 900px; overflow: hidden; background: var(--page); }
  body { position: relative; font-family: "Jost", "Helvetica Neue", Arial, sans-serif; }

  .card-front {
    position: absolute; left: -75px; top: 211px;
    width: 820px; height: 478px;
    transform: rotate(-90deg);
    background: var(--panel);
  }
  .front-band { position: absolute; left: 0; top: 0; width: 820px; height: 194px; background: var(--band-light); }
  .front-edge { position: absolute; left: 0; bottom: 0; width: 820px; height: 30px; background: var(--edge); }

  .company-name {
    position: absolute; left: 44px; top: 80px;
    color: var(--ink-light); font-weight: 300; font-size: 28px; line-height: 1;
  }

  .person { position: absolute; left: 50px; top: 256px; color: var(--ink-light); }
  .person-name { font-weight: 400; font-size: 33px; letter-spacing: 0.5px; line-height: 1.1; }
  .person-title { font-weight: 300; font-size: 22px; margin-top: 6px; }

  .contact {
    position: absolute; left: 380px; top: 246px; width: 400px;
    padding-top: 10px; font-size: 11px; letter-spacing: 0.6px; color: var(--ink-soft);
  }
  .contact::before {
    content: ""; position: absolute; left: 0; top: 0; width: 170px; height: 1px; background: var(--ink-muted);
  }
  .contact-row { display: flex; height: 30px; align-items: center; white-space: nowrap; }
  .contact-label { width: 32px; color: var(--ink-muted); border-right: 1px solid var(--ink-muted); margin-right: 10px; }

  .card-back {
    position: absolute; left: 620px; top: 40px;
    width: 480px; height: 820px; background: var(--back); overflow: hidden;
  }
  .back-stripes { position: absolute; left: 0; top: 0; }
  .back-mark {
    position: absolute; left: 240px; top: 410px;
    transform: translate(-50%, -50%) rotate(-90deg);
    color: var(--mark); font-weight: 400; font-size: 120px; line-height: 1;
  }
</style>
</head>
<body>
  <section class="card-front" aria-label="Card front">
    <div class="front-band"></div>
    <div class="front-edge"></div>

    <div class="company-name">The Kestrel Bureau</div>

    <div class="person">
      <div class="person-name">Dr. Mara Ellison</div>
      <div class="person-title">Director</div>
    </div>

    <div class="contact">
      <div class="contact-row"><span class="contact-label">Mo:</span><span>+61 400 555 123</span></div>
      <div class="contact-row"><span class="contact-label">Ph:</span><span>+61 2 5550 1234</span></div>
      <div class="contact-row"><span class="contact-label">Em:</span><span>mara@kestrelbureau.com.au</span></div>
      <div class="contact-row"><span class="contact-label">PO:</span><span>P.O. Box 418, Lindfield West, Sydney, Australia</span></div>
    </div>
  </section>

  <section class="card-back" aria-label="Card back">
    <svg class="back-stripes" width="480" height="820" viewBox="0 0 480 820">
      <g fill="var(--stripe)">
        <rect x="212" y="0" width="6" height="820"/>
        <rect x="232" y="0" width="6" height="820"/>
        <rect x="252" y="0" width="6" height="820"/>
        <rect x="272" y="0" width="6" height="820"/>
        <rect x="292" y="0" width="6" height="820"/>
        <rect x="312" y="0" width="6" height="820"/>
        <rect x="336" y="0" width="6" height="820"/>
        <rect x="360" y="0" width="6" height="820"/>
        <rect x="386" y="0" width="6" height="820"/>
        <rect x="406" y="0" width="6" height="820"/>
      </g>
    </svg>
    <div class="back-mark">KLB</div>
  </section>
</body>
</html>
```